Webdesign for Dutch IT consultancy company

Make a Wordpress webdesign for a Dutch consultancy company

Briefing Velmora IT

Website for finding and connecting IT-professionals. Corebusiness is to find IT-professionals and to help them to follow their ambitions. We offer training, personal coaching and education trajects.

U can take www.Tralvique.nl as an example for the website.

Home page

U can take www.Tralvique.nl as an example.

There should be jobs on the home page. A block for short info about us and about what whe do and a trigger to contact us quickly.

Jobs Page

On this page should be the jobs that we offer for the professionals. There should be a search function on this page so u can easily find the job that you are looking for.

A call to action can be on this page too.

Also a little block with text for some information.

For professionals page

Block with information on top. Call to action. info about who we work for/with.

For Clients

Info about three different solutions

- Sourcing solutions
- Consultancy solutions
- Custom based traineeships

Request a qoute option

Traineeships page

Info about two different traineeships

- Linux traineeships
- Microsoft traineeships

Call to action/ subscribe for traineeships

About us page

We are Velmora IT

Our mission: Creating cooperations between young professionals and businesses who wanna work on a great future.

Our core values

Last news

Target Market(s)

Young professionals and businesses who need IT services

Industry/Entity Type

It Company

Coding

Coded - Design and coding required

Number of Pages Required

5+ page

Font styles to use
Other font styles liked:
• Calibri

Colors
ffffff
add136
6b449b

Requirements
Must have
• Home page, Jobs Page, Professionals page, Clients page, Traineeships page, About us Page
• Green and/or Purple layout. Job search option, subscribe option
Nice to have
• modern design

```html
<!DOCTYPE html>
<html lang="en">
<head>
<meta charset="utf-8">
<title>Velmora IT – Sourcing | Consultancy</title>
<link rel="stylesheet" href="https://fonts.googleapis.com/css2?family=Carlito:wght@400;700&family=Open+Sans:wght@400;600;700&display=swap">
<style>
:root{
  --purple:#6b449b;
  --purple-dark:#5a3787;
  --green:#add136;
  --white:#ffffff;
  --ink:#3a3a3a;
  --muted:#666666;
  --light-bg:#f4f4f4;
  --footer-bg:#262626;
  --bottom-bg:#141414;
  --footer-text:#d6d6d6;
}
*{margin:0;padding:0;box-sizing:border-box}
html,body{width:1200px;height:2179px;overflow:hidden}
body{position:relative;background:var(--white);font-family:"Carlito","Calibri",sans-serif;color:var(--ink)}
.abs{position:absolute}

/* header */
.site-header{position:absolute;left:0;top:0;width:1200px;height:73px;background:var(--white);box-shadow:0 1px 3px rgba(0,0,0,.08);z-index:2}
.brand{position:absolute;left:161px;top:20px;display:flex;align-items:center;gap:8px}
.brand-mark{width:22px;height:22px;background:var(--purple);border-radius:4px}
.brand-name{font-family:"Carlito",sans-serif;font-weight:700;font-size:28px;color:var(--purple);letter-spacing:.5px}
.main-nav{position:absolute;top:0;left:580px;height:73px;display:flex}
.main-nav a{position:relative;display:block;line-height:73px;padding:0 13px;font-family:"Open Sans",sans-serif;font-size:10px;color:#555;text-decoration:none;text-transform:uppercase}
.main-nav a.active::after{content:"";position:absolute;left:0;right:0;bottom:0;height:4px;background:var(--green)}

/* hero */
.hero{position:absolute;left:0;top:73px;width:1200px;height:581px;overflow:hidden}
.hero-photo{position:absolute;inset:0;background:linear-gradient(100deg,#8e9091 0%,#a7a8a6 35%,#9b9894 60%,#b4b2ae 80%,#8d8c8a 100%)}
.hero-shade{position:absolute;inset:0;background:rgba(60,60,60,.25)}
.hero-title{position:absolute;left:0;width:1200px;top:250px;text-align:center;font-family:"Open Sans",sans-serif;font-weight:700;font-size:58px;line-height:70px;color:var(--white);letter-spacing:1px}
.hero-title .accent{color:var(--green)}
.hero-sub{position:absolute;left:0;width:1200px;top:330px;text-align:center;font-family:"Open Sans",sans-serif;font-size:11.5px;line-height:20px;color:var(--white);text-transform:uppercase}
.btn{display:inline-block;background:var(--green);color:var(--white);text-align:center;text-transform:uppercase;text-decoration:none}
.hero-btn{position:absolute;left:530px;top:399px;width:140px;height:41px;line-height:41px;font-family:"Open Sans",sans-serif;font-weight:600;font-size:10px}
.hero-arrow{position:absolute;top:282px;width:24px;height:44px}

/* search */
.job-search{position:absolute;left:0;top:654px;width:1200px;height:109px;background:var(--purple)}
.search-fields{position:absolute;left:161px;top:35px;width:653px;height:41px;background:var(--white);display:flex;border-radius:2px;box-shadow:0 2px 0 rgba(0,0,0,.15)}
.search-field{height:41px;line-height:41px;padding-left:10px;font-family:"Open Sans",sans-serif;font-size:9.5px;color:#555;text-transform:uppercase;border-right:1px solid #ddd;position:relative}
.search-field:last-child{border-right:none}
.search-field.keywords{width:213px}
.search-field.location{width:224px}
.search-field.category{width:216px}
.search-field.category svg{position:absolute;right:12px;top:17px}
.search-btn{position:absolute;left:837px;top:35px;width:202px;height:41px;line-height:41px;font-family:"Open Sans",sans-serif;font-size:13px;box-shadow:0 2px 0 rgba(0,0,0,.2)}
.search-btn svg{vertical-align:-3px;margin-right:12px}

/* section headings */
.section-head{position:absolute;left:0;width:1200px;text-align:center}
.section-head .dot{display:block;margin:0 auto;width:26px;height:26px;border-radius:50%;background:var(--purple)}
.section-head h2{margin-top:10px;font-family:"Open Sans",sans-serif;font-weight:600;font-size:20px;letter-spacing:1px;color:var(--purple);text-transform:uppercase}
.section-head h2 span{color:var(--green);font-weight:400}
.section-head .rule{display:block;margin:6px auto 0;width:78px;height:1px;background:var(--purple)}

/* about */
.about-media{position:absolute;left:163px;top:933px;width:422px;height:274px;background:linear-gradient(135deg,#9aa3a6 0%,#d6d2cc 40%,#b79c8a 65%,#7d8a95 100%)}
.play{position:absolute;left:188px;top:114px;width:46px;height:46px;border-radius:50%;background:rgba(255,255,255,.8)}
.play svg{position:absolute;left:17px;top:14px}
.about-copy{position:absolute;left:613px;top:938px;width:430px}
.about-copy h3{font-weight:400;font-size:17px;color:#333;letter-spacing:.3px}
.about-copy p{margin-top:15px;font-size:12px;line-height:18px;color:#444}
.about-copy p + p{margin-top:17px}
.read-more{position:absolute;left:613px;top:1148px;width:108px;height:37px;line-height:37px;font-size:11.5px}

/* services */
.services{position:absolute;left:0;top:1247px;width:1200px;height:402px;background:var(--light-bg)}
.service{position:absolute;top:185px;width:300px;text-align:center}
.service .icon{display:block;margin:0 auto;width:72px;height:72px}
.service h4{margin-top:14px;font-family:"Open Sans",sans-serif;font-weight:400;font-size:12px;color:#555;text-transform:uppercase;letter-spacing:.5px}
.service p{margin-top:10px;font-family:"Open Sans",sans-serif;font-size:9.5px;line-height:21px;color:#555;text-transform:uppercase}

/* contact band */
.contact-band{position:absolute;left:0;top:1649px;width:1200px;height:151px;background:linear-gradient(90deg,#6e4a9e 0%,#7a56a8 50%,#6b449b 100%)}
.contact-band .texture{position:absolute;inset:0;background:radial-gradient(circle at 30% 40%,rgba(255,255,255,.08),transparent 40%),radial-gradient(circle at 75% 60%,rgba(255,255,255,.07),transparent 45%)}
.contact-text{position:absolute;left:260px;top:66px;font-family:"Open Sans",sans-serif;font-size:15px;color:var(--white);text-transform:uppercase;letter-spacing:.5px}
.contact-btn{position:absolute;left:657px;top:55px;width:202px;height:42px;line-height:42px;font-family:"Open Sans",sans-serif;font-size:13px}
.contact-btn svg{vertical-align:-3px;margin-right:14px}

/* footer */
.site-footer{position:absolute;left:0;top:1800px;width:1200px;height:314px;background:var(--footer-bg);color:var(--footer-text)}
.footer-col{position:absolute;top:28px}
.footer-col h5{font-family:"Open Sans",sans-serif;font-weight:700;font-size:10.5px;color:var(--white);text-transform:uppercase;letter-spacing:.8px}
.footer-col h5::after{content:"";display:block;width:14px;height:2px;background:var(--white);margin-top:5px}
.footer-text{font-family:"Open Sans",sans-serif;font-size:10px;line-height:19px;color:var(--footer-text)}
.footer-brand{margin-top:22px;font-family:"Carlito",sans-serif;font-weight:700;font-size:22px;color:#e8e8e8}
.about-col .footer-text{margin-top:20px;width:200px}
.reach-list{list-style:none;margin-top:22px}
.reach-list li{position:relative;padding-left:26px;margin-bottom:12px;font-family:"Open Sans",sans-serif;font-size:10.5px;line-height:16px}
.reach-list svg{position:absolute;left:0;top:2px}
.links-list{list-style:none;margin-top:20px}
.links-list li{position:relative;padding-left:26px;height:25.5px;font-family:"Open Sans",sans-serif;font-size:10px;line-height:14px}
.links-list svg{position:absolute;left:0;top:1px}
.newsletter .footer-text{margin-top:18px}
.subscribe{margin-top:16px;width:202px;height:33px;border:2px solid var(--white);position:relative;font-family:"Open Sans",sans-serif;font-size:9px;line-height:29px;padding-left:7px;color:var(--white)}
.subscribe svg{position:absolute;right:8px;top:8px}
.footer-rule{position:absolute;left:161px;top:215px;width:878px;height:1px;background:#3d3d3d}
.follow{position:absolute;left:0;top:235px;width:1200px;text-align:center;font-family:"Open Sans",sans-serif;font-weight:700;font-size:10.5px;color:var(--white);text-transform:uppercase;letter-spacing:.8px}
.social{position:absolute;left:526px;top:268px;display:flex;gap:7px}
.social span{display:block;width:24px;height:24px;border:1px solid #bbb}
.bottom-bar{position:absolute;left:0;top:2114px;width:1200px;height:65px;background:var(--bottom-bg);text-align:center;line-height:65px;font-family:"Open Sans",sans-serif;font-size:10px;color:#ddd}
</style>
</head>
<body>

<header class="site-header">
  <div class="brand"><span class="brand-mark"></span><span class="brand-name">Velmora IT</span></div>
  <nav class="main-nav">
    <a class="active" href="#">Home</a>
    <a href="#">About</a>
    <a href="#">What we do</a>
    <a href="#">Jobs</a>
    <a href="#">Clients</a>
    <a href="#">Traineeships</a>
    <a href="#">Contact</a>
  </nav>
</header>

<section class="hero">
  <div class="hero-photo" role="img" aria-label="Photo of two smiling colleagues working together at a laptop in a bright office"></div>
  <div class="hero-shade"></div>
  <svg class="hero-arrow" style="left:26px" viewBox="0 0 24 44"><path d="M22 2 2 22l20 20" fill="none" stroke="#fff" stroke-width="2.5"/></svg>
  <svg class="hero-arrow" style="left:1152px" viewBox="0 0 24 44"><path d="M2 2l20 20L2 42" fill="none" stroke="#fff" stroke-width="2.5"/></svg>
  <h1 class="hero-title"><span class="accent">LOREM</span> IPSUM</h1>
  <p class="hero-sub">Velmora theme is providing you the best directory services from<br>good leading companies</p>
  <a class="btn hero-btn" href="#">View vacancies</a>
</section>

<section class="job-search">
  <div class="search-fields">
    <div class="search-field keywords">Keywords</div>
    <div class="search-field location">Location</div>
    <div class="search-field category">Category
      <svg width="8" height="6" viewBox="0 0 8 6"><path d="M1 1l3 3 3-3" fill="none" stroke="#444" stroke-width="1.4"/></svg>
    </div>
  </div>
  <a class="btn search-btn" href="#"><svg width="16" height="16" viewBox="0 0 16 16"><circle cx="6.5" cy="6.5" r="5" fill="none" stroke="#fff" stroke-width="2.2"/><path d="M10.3 10.3 15 15" stroke="#fff" stroke-width="2.6" stroke-linecap="round"/></svg>Search</a>
</section>

<section class="about">
  <div class="section-head" style="top:811px">
    <span class="dot"></span>
    <h2>About <span>ourself</span></h2>
    <span class="rule"></span>
  </div>
  <div class="about-media" role="img" aria-label="Photo of a team of young professionals meeting around a table with a tablet">
    <div class="play"><svg width="14" height="18" viewBox="0 0 14 18"><path d="M1 1l12 8-12 8z" fill="#555"/></svg></div>
  </div>
  <div class="about-copy">
    <h3>Lorem Ipsum is simply dummy text</h3>
    <p>Lorem ipsum dolor sit amet, consectetur adipisicing elit simil ique non distinctio adipisicing elit. Quas vtem maioeaque similique non distinctio voluptates</p>
    <p>Lorem ipsum dolor sit amet, consectetur adipisicing elit. Praesentium, sed ad iure dignissimos! Maxime nesciunt ex id perspiciatis ratione. Quia, beatae sint? Voluptatem possimus delectus, necessitatibus asperiores accusamus porro voluptas fugiat nobis unde! Quidem, qui ab. Voluptate, nihil?</p>
  </div>
  <a class="btn read-more" href="#">Read more</a>
</section>

<section class="services">
  <div class="section-head" style="top:38px">
    <span class="dot"></span>
    <h2>What <span>we do</span></h2>
    <span class="rule"></span>
  </div>
  <div class="service" style="left:149px">
    <svg class="icon" viewBox="0 0 72 72" role="img" aria-label="Icon of a trainer at a board"><circle cx="36" cy="36" r="34" fill="#fff" stroke="var(--purple)" stroke-width="2"/><circle cx="36" cy="36" r="18" fill="#e6ddf0"/></svg>
    <h4>Training</h4>
    <p>Lorem ipsum dolor sit ametconsect etur<br>adipisicing elit, numquam modi consequuntur<br>maxime voluptates earum illo sunt</p>
  </div>
  <div class="service" style="left:450px">
    <svg class="icon" viewBox="0 0 72 72" role="img" aria-label="Icon of two people in a coaching conversation"><circle cx="36" cy="36" r="34" fill="#fff" stroke="var(--purple)" stroke-width="2"/><circle cx="36" cy="36" r="18" fill="#e6ddf0"/></svg>
    <h4>Personal coaching</h4>
    <p>Lorem ipsum dolor sit ametconsect etur<br>adipisicing elit, numquam modi consequuntur<br>maxime voluptates earum illo sunt</p>
  </div>
  <div class="service" style="left:749px">
    <svg class="icon" viewBox="0 0 72 72" role="img" aria-label="Icon of a graduate in cap and gown"><circle cx="36" cy="36" r="34" fill="#fff" stroke="var(--purple)" stroke-width="2"/><circle cx="36" cy="36" r="18" fill="#e6ddf0"/></svg>
    <h4>Education trajects</h4>
    <p>Lorem ipsum dolor sit ametconsect etur<br>adipisicing elit, numquam modi consequuntur<br>maxime voluptates earum illo sunt</p>
  </div>
</section>

<section class="contact-band" role="img" aria-label="Purple tinted photo of a crowd of people">
  <div class="texture"></div>
  <p class="contact-text">Nullam at nunc at nulla facilisis accumsan.</p>
  <a class="btn contact-btn" href="#"><svg width="18" height="13" viewBox="0 0 18 13"><rect x="1" y="1" width="16" height="11" fill="none" stroke="#fff" stroke-width="1.6"/><path d="M1 1l8 6 8-6" fill="none" stroke="#fff" stroke-width="1.6"/></svg>Contact us</a>
</section>

<footer class="site-footer">
  <div class="footer-col about-col" style="left:161px">
    <h5>About us</h5>
    <div class="footer-brand">Velmora IT</div>
    <p class="footer-text">There are many variations of passages of Lorem Ipsum available, but the majority have suffered alteration in some form</p>
  </div>
  <div class="footer-col" style="left:389px">
    <h5>Reach au at</h5>
    <ul class="reach-list">
      <li><svg width="9" height="13" viewBox="0 0 9 13"><path d="M4.5 0A4.5 4.5 0 0 0 0 4.5C0 8 4.5 13 4.5 13S9 8 9 4.5A4.5 4.5 0 0 0 4.5 0z" fill="#ddd"/><circle cx="4.5" cy="4.5" r="1.7" fill="#262626"/></svg>There are many variations of<br>passages of Lorem Ipsum available</li>
      <li><svg width="11" height="11" viewBox="0 0 11 11"><path d="M2.2 0 4 2.8 2.8 4.2a7 7 0 0 0 4 4L8.2 7 11 8.8 9.8 11C4.5 11 0 6.5 0 1.2z" fill="#ddd"/></svg>999-999-9999</li>
      <li><svg width="12" height="9" viewBox="0 0 12 9"><rect x=".6" y=".6" width="10.8" height="7.8" fill="none" stroke="#ddd" stroke-width="1.2"/><path d="M.6.6 6 5l5.4-4.4" fill="none" stroke="#ddd" stroke-width="1.2"/></svg>info@yourdomain.com</li>
    </ul>
  </div>
  <div class="footer-col" style="left:612px">
    <h5>Quick links</h5>
    <ul class="links-list">
      <li><svg width="11" height="11" viewBox="0 0 11 11"><circle cx="5.5" cy="5.5" r="5.5" fill="#ddd"/><path d="M4 3l3 2.5L4 8" fill="none" stroke="#262626" stroke-width="1.5"/></svg>Working at Tralvique in the office</li>
      <li><svg width="11" height="11" viewBox="0 0 11 11"><circle cx="5.5" cy="5.5" r="5.5" fill="#ddd"/><path d="M4 3l3 2.5L4 8" fill="none" stroke="#262626" stroke-width="1.5"/></svg>IT Traineeship</li>
      <li><svg width="11" height="11" viewBox="0 0 11 11"><circle cx="5.5" cy="5.5" r="5.5" fill="#ddd"/><path d="M4 3l3 2.5L4 8" fill="none" stroke="#262626" stroke-width="1.5"/></svg>Technical Traineeship</li>
      <li><svg width="11" height="11" viewBox="0 0 11 11"><circle cx="5.5" cy="5.5" r="5.5" fill="#ddd"/><path d="M4 3l3 2.5L4 8" fill="none" stroke="#262626" stroke-width="1.5"/></svg>Training &amp; training</li>
      <li><svg width="11" height="11" viewBox="0 0 11 11"><circle cx="5.5" cy="5.5" r="5.5" fill="#ddd"/><path d="M4 3l3 2.5L4 8" fill="none" stroke="#262626" stroke-width="1.5"/></svg>Job tips</li>
    </ul>
  </div>
  <div class="footer-col newsletter" style="left:837px">
    <h5>Newsletter</h5>
    <p class="footer-text">Subscribe our newsletter!<br>There are many variations of passages<br>of Lorem Ipsum available,</p>
    <div class="subscribe">Email Address
      <svg width="13" height="13" viewBox="0 0 13 13"><circle cx="6.5" cy="6.5" r="6.5" fill="var(--green)"/><path d="M3.5 6.5h5M6.5 4l2.5 2.5L6.5 9" fill="none" stroke="#262626" stroke-width="1.6"/></svg>
    </div>
  </div>
  <div class="footer-rule"></div>
  <p class="follow">Follow us on</p>
  <div class="social" aria-label="Social media links"><span></span><span></span><span></span><span></span><span></span></div>
</footer>

<div class="bottom-bar">© 2017 Velmora IT. All Rights Reserved.</div>

</body>
</html>
```